Project Title:
Dental Implant Overdenture Flyer (Retirement Village Target)
Objective:
Create a clean, trustworthy, and reassuring flyer aimed at older adults (60–85 years old) who struggle with loose dentures. The goal is to educate them about implant-retained “clip-on” dentures and encourage them to book a consultation.
Tone & Feel:
Warm, caring, non-intimidating
Premium but not “salesy”
Medical but easy to understand
Focus on improving quality of life (confidence, eating, comfort)
Target Audience:
Retirees / pensioners
Existing denture wearers
People frustrated with loose or uncomfortable dentures
Key Message:
“You don’t have to live with loose dentures anymore.”
Design Style:
Clean, minimal, modern
Soft colours (blues, greens, warm neutrals)
Easy-to-read large font
High contrast for older eyes
Avoid clutter
Imagery Suggestions:
Smiling older adults (natural, not stocky/overly staged)
Before/after lifestyle (eating, laughing, socialising)
Simple diagram showing denture clipping onto implants
Avoid graphic surgical images
Layout Suggestions:
A5 or DL flyer
Clear sections with headings
Icons for benefits
Strong call-to-action at bottom
HEADLINE (big and bold)
Tired of Loose Dentures?
Discover Secure “Clip-On” Teeth
🔹 PROBLEM SECTION
Do your dentures:
Slip or move when eating?
Make it hard to chew certain foods?
Feel uncomfortable or loose?
Affect your confidence when speaking or smiling?
You’re not alone — and there is a better solution.
🔹 SOLUTION SECTION
Implant-Retained “Clip-On” Dentures
We can secure your denture using just 2 dental implants, allowing your teeth to:
✔ Stay firmly in place
✔ Improve your ability to eat
✔ Feel more comfortable
✔ Boost your confidence
🔹 SIMPLE EXPLANATION (very important)
Small titanium implants are gently placed in the jaw.
Your denture then clips securely onto them, stopping movement.
🔹 PRICE SECTION (highlight this clearly)
$12,000
Includes:
2 dental implants
A brand new custom overdenture
Does not include sedation or extractions (if needed)
🔹 SEDATION
Sedation is available for comfort.
If you hold a pensioner card, you may receive a significant Vantacor rebate, often resulting in minimal out-of-pocket costs for sedation.
🔹 TRUST / REASSURANCE
Experienced implant clinician
Gentle, patient-focused care
Modern technology and techniques
🔹 CALL TO ACTION (VERY IMPORTANT)
Book a Free Consultation
📞 Call: 08 9351 4276
🌐 Visit: www.bravonclinic.com.au
📍 Located near Tallowmere shopping centre
🔹 OPTIONAL TAGLINE
Eat Better. Feel Better. Smile with Confidence Again.
Please include some photos to illustrate what a clip on denture looks like with two implants.

```html
<!DOCTYPE html>
<html lang="en">
<head>
<meta charset="utf-8">
<title>Implant-Retained Clip-On Dentures Flyer</title>
<link href="https://fonts.googleapis.com/css2?family=Gelasio:wght@700&family=Jost:ital,wght@0,400;0,500;0,600;1,400&display=swap" rel="stylesheet">
<style>
  :root {
    --teal: #1796b0;
    --ink: #1f1f1f;
    --charcoal: #4d4d4d;
    --paper: #faf7f6;
    --card: #ffffff;
    --price-body: #dedede;
    --white: #ffffff;
  }
  * { margin: 0; padding: 0; box-sizing: border-box; }
  html, body { width: 849px; height: 1200px; overflow: hidden; }
  body { font-family: "Jost", sans-serif; color: var(--ink); background: var(--paper); }
  .flyer { position: relative; width: 849px; height: 1200px; overflow: hidden; background: var(--paper); }
  .abs { position: absolute; }

  .hero-backdrop { left: 0; top: 0; width: 849px; height: 452px;
    background: linear-gradient(90deg, #f9f6f5 0%, #f3f1f0 30%, #dde6ec 55%, #cfdde6 100%); }
  .hero-photo { left: 330px; top: 0; width: 519px; height: 452px;
    background: radial-gradient(ellipse at 45% 45%, #e9d3c6 0%, #d6c6bb 30%, #b9c9d8 60%, rgba(200,215,226,0) 85%); }

  .brand { left: 46px; top: 80px; display: flex; align-items: center; gap: 10px; }
  .brand-dot { width: 26px; height: 26px; border-radius: 50%; background: var(--teal); }
  .brand-name { font-size: 17px; font-weight: 500; color: var(--teal); letter-spacing: 1.5px; text-transform: uppercase; }

  .headline { left: 40px; top: 205px; font-family: "Gelasio", serif; font-weight: 700; font-size: 55px; line-height: 52px; color: var(--ink); }
  .subhead { left: 40px; top: 318px; font-size: 36px; font-weight: 500; line-height: 37px; color: var(--teal); }

  .problem-card { left: 0; top: 413px; width: 394px; height: 503px; background: var(--card); border-radius: 0 24px 24px 0; }
  .problem-title { left: 38px; top: 430px; font-size: 22px; font-weight: 500; }
  .problem-list { left: 113px; top: 470px; list-style: none; font-size: 17px; line-height: 18px; }
  .problem-list li { margin-bottom: 11px; }
  .reassure { left: 38px; top: 615px; font-size: 21px; font-weight: 600; line-height: 22px; }
  .diagram { left: 118px; top: 674px; width: 175px; height: 198px; border-radius: 10px 10px 60px 60px;
    background: linear-gradient(180deg, #f2e4e4 0%, #f49a9a 35%, #ffffff 52%, #f28f8f 70%, #efe0e0 100%); }

  .solution-title { left: 409px; top: 472px; font-size: 22.5px; font-weight: 600; letter-spacing: .3px; }
  .solution-intro { left: 409px; top: 504px; font-size: 17px; line-height: 17px; width: 400px; }
  .ticks { list-style: none; }
  .ticks li { display: flex; align-items: center; gap: 12px; }
  .ticks svg { flex: none; }
  .solution-ticks { left: 414px; top: 548px; font-size: 17px; }
  .solution-ticks li { height: 22.5px; }
  .simple-title { left: 409px; top: 651px; font-size: 18px; font-weight: 600; }
  .simple-text { left: 409px; top: 675px; font-size: 12.5px; line-height: 17px; width: 320px; }

  .dark-band { left: 0; top: 865px; width: 849px; height: 335px; background: var(--charcoal); }

  .price-box { left: 424px; top: 727px; width: 339px; height: 193px; border-radius: 24px; overflow: hidden; background: var(--price-body); }
  .price-head { height: 52px; background: var(--teal); color: var(--white); font-size: 38px; font-weight: 600; text-align: center; line-height: 52px; }
  .price-includes { position: absolute; left: 18px; top: 62px; font-size: 23px; font-weight: 600; }
  .price-ticks { position: absolute; left: 26px; top: 95px; font-size: 16.5px; }
  .price-ticks li { height: 22px; gap: 10px; }
  .price-note { position: absolute; left: 33px; top: 148px; font-size: 14.5px; font-style: italic; line-height: 16px; color: #333; }

  .comfort-title { left: 41px; top: 920px; font-size: 22px; font-weight: 500; line-height: 24px; color: var(--white); }
  .comfort-text { left: 41px; top: 987px; width: 345px; font-size: 13px; line-height: 15.5px; color: var(--white); }
  .why-title { left: 41px; top: 1074px; font-size: 22px; font-weight: 500; color: var(--white); }
  .why-ticks { left: 41px; top: 1104px; font-size: 14px; color: var(--white); }
  .why-ticks li { height: 18px; gap: 8px; }

  .cta { left: 480px; top: 938px; width: 283px; height: 40px; border-radius: 10px; background: var(--teal); color: var(--white);
    font-size: 22px; text-align: center; line-height: 40px; }
  .contacts { left: 500px; top: 990px; list-style: none; color: var(--white); font-size: 18.5px; }
  .contacts li { display: flex; align-items: center; gap: 14px; margin-bottom: 8px; line-height: 19px; }
  .contacts svg { flex: none; width: 26px; height: 26px; }
  .tagline { left: 443px; top: 1102px; font-size: 12.5px; font-style: italic; color: var(--white); }
</style>
</head>
<body>
<main class="flyer">
  <div class="abs hero-backdrop"></div>
  <div class="abs hero-photo" role="img" aria-label="Photo of a smiling older couple embracing outdoors"></div>

  <div class="abs brand"><span class="brand-dot"></span><span class="brand-name">Bravon Dental Surgery</span></div>

  <h1 class="abs headline">Tired of Loose<br>Dentures?</h1>
  <p class="abs subhead">Discover Secure<br>Clip-On Teeth</p>

  <section>
    <div class="abs problem-card"></div>
    <h2 class="abs problem-title">Do your dentures:</h2>
    <ul class="abs problem-list">
      <li>Slip or move when eating?</li>
      <li>Make it hard to chew certain foods?</li>
      <li>Feel uncomfortable or loose?</li>
      <li>Affect your confidence when<br>speaking or smiling?</li>
    </ul>
    <p class="abs reassure">You’re not alone — and there is<br>a better solution.</p>
    <div class="abs diagram" role="img" aria-label="Illustration of a full denture clipping onto implants in the jaw"></div>
  </section>

  <section>
    <h2 class="abs solution-title">Implant-Retained Clip-On Dentures</h2>
    <p class="abs solution-intro">We can secure your denture using just 2 dental implants, allowing your teeth to:</p>
    <ul class="abs ticks solution-ticks">
      <li><svg width="16" height="16" viewBox="0 0 16 16"><path d="M1 9l4 5L15 1" fill="none" stroke="#1f1f1f" stroke-width="1.6"/></svg>Stay firmly in place</li>
      <li><svg width="16" height="16" viewBox="0 0 16 16"><path d="M1 9l4 5L15 1" fill="none" stroke="#1f1f1f" stroke-width="1.6"/></svg>Improve your ability to eat</li>
      <li><svg width="16" height="16" viewBox="0 0 16 16"><path d="M1 9l4 5L15 1" fill="none" stroke="#1f1f1f" stroke-width="1.6"/></svg>Feel more comfortable</li>
      <li><svg width="16" height="16" viewBox="0 0 16 16"><path d="M1 9l4 5L15 1" fill="none" stroke="#1f1f1f" stroke-width="1.6"/></svg>Boost your confidence</li>
    </ul>
    <h3 class="abs simple-title">Simple, Secure, Effective</h3>
    <p class="abs simple-text">Small titanium implants are gently placed in the jaw. Your denture then clips securely onto them — stopping movement and restoring stability.</p>
  </section>

  <div class="abs dark-band"></div>

  <section class="abs price-box">
    <div class="price-head">$12,000</div>
    <h3 class="price-includes">Includes:</h3>
    <ul class="ticks price-ticks">
      <li><svg width="15" height="15" viewBox="0 0 16 16"><path d="M1 9l4 5L15 1" fill="none" stroke="#1f1f1f" stroke-width="1.8"/></svg>2 dental implants</li>
      <li><svg width="15" height="15" viewBox="0 0 16 16"><path d="M1 9l4 5L15 1" fill="none" stroke="#1f1f1f" stroke-width="1.8"/></svg>A brand new custom overdenture</li>
    </ul>
    <p class="price-note">Does not include sedation or extractions<br>(if needed)</p>
  </section>

  <section>
    <h2 class="abs comfort-title">Comfortable, Stress-Free<br>Treatment</h2>
    <p class="abs comfort-text">Sedation is available to ensure a relaxed experience. If you hold a pensioner card, you may be eligible for a Vantacor rebate, often resulting in minimal out-of-pocket costs for sedation.</p>
    <h2 class="abs why-title">Why Choose Us</h2>
    <ul class="abs ticks why-ticks">
      <li><svg width="13" height="13" viewBox="0 0 16 16"><path d="M1 9l4 5L15 1" fill="none" stroke="#fff" stroke-width="1.6"/></svg>Experienced implant clinician</li>
      <li><svg width="13" height="13" viewBox="0 0 16 16"><path d="M1 9l4 5L15 1" fill="none" stroke="#fff" stroke-width="1.6"/></svg>Gentle, patient-focused care</li>
      <li><svg width="13" height="13" viewBox="0 0 16 16"><path d="M1 9l4 5L15 1" fill="none" stroke="#fff" stroke-width="1.6"/></svg>Modern technology and techniques</li>
    </ul>
  </section>

  <section>
    <div class="abs cta">Book a Free Consultation</div>
    <ul class="abs contacts">
      <li><svg viewBox="0 0 24 24"><path d="M6.5 2.5l3 4-2 2.5c1.2 2.6 3.5 4.9 6 6l2.5-2 4 3-1.5 3.5c-8 0-15.5-7.5-15.5-15.5z" fill="#fff"/></svg>08 9351 4276</li>
      <li><svg viewBox="0 0 24 24" fill="none" stroke="#fff" stroke-width="1.5"><circle cx="12" cy="12" r="10"/><ellipse cx="12" cy="12" rx="4.5" ry="10"/><path d="M2 12h20M4 7h16M4 17h16"/></svg>www.bravonclinic.com.au</li>
      <li><svg viewBox="0 0 24 24" fill="none" stroke="#fff" stroke-width="1.5"><path d="M12 21s-7-7-7-12a7 7 0 0114 0c0 5-7 12-7 12z"/><circle cx="12" cy="9" r="2.5"/><path d="M7 21h10"/></svg>Located near Tallowmere<br>Shopping Centre</li>
    </ul>
    <p class="abs tagline">Eat Better. Feel Better. Smile with Confidence Again.</p>
  </section>
</main>
</body>
</html>
```